Lark Hollow Edibles product label

We are looking to create a product label for a new product. We are a THC edible company. Labels must not contain anything that resembles marijuana. Labels also must not contain anything that is appealing to children. The state is very strict. I want a professional label but also fun.

What the label must include.
Logo/Name (I will provide that in a file)
Dose: 50mg per pack
Servings: 10 servings per pack
Warning label for kids
Assorted flavors

Please be creative. Label size will need to be 3" wide and 5" tall.

```html
<!DOCTYPE html>
<html lang="en">
<head>
<meta charset="utf-8">
<title>Lark Hollow Edibles – THC Gummies Label</title>
<link rel="stylesheet" href="https://fonts.googleapis.com/css2?family=Bebas+Neue&family=Montserrat:wght@500;600;700;800;900&display=swap">
<style>
  :root {
    --navy: #1c3a64;
    --navy-deep: #163257;
    --pink: #e1457f;
    --red: #d9362f;
    --white: #ffffff;
    --page: #ffffff;
    --fruit-light: #f3e4e8;
    --fruit-mid: #e7a9b4;
    --fruit-deep: #c9566a;
  }
  * { box-sizing: border-box; margin: 0; padding: 0; }
  html, body {
    width: 1200px; height: 1200px; overflow: hidden;
    background: var(--page);
    font-family: "Montserrat", sans-serif;
  }
  .label {
    position: absolute;
    left: 324px; top: 50px;
    width: 552px; height: 1085px;
    background: var(--white);
    overflow: hidden;
    box-shadow: 0 14px 26px rgba(0,0,0,0.22);
  }
  .fruit-backdrop {
    position: absolute; left: 0; top: 0; width: 552px; height: 837px;
    background: linear-gradient(160deg, var(--fruit-light) 0%, var(--fruit-mid) 55%, var(--fruit-deep) 100%);
  }
  .pennant {
    position: absolute; left: 90px; top: 0; width: 371px; height: 535px;
  }
  .brand {
    position: absolute; left: 90px; top: 86px; width: 371px;
    display: flex; align-items: center; justify-content: center; gap: 12px;
    color: var(--white);
  }
  .brand-mark { width: 50px; height: 50px; background: var(--white); }
  .brand-name {
    font-weight: 700; font-size: 23px; line-height: 1.05;
    letter-spacing: 0.5px; text-transform: uppercase;
  }
  .brand-name span { display: block; font-size: 15px; letter-spacing: 5px; }
  .product-thc, .product-gummies {
    position: absolute; left: 90px; width: 371px;
    text-align: center; color: var(--white);
    font-family: "Bebas Neue", sans-serif; font-weight: 400; line-height: 1;
  }
  .product-thc { top: 170px; font-size: 165px; letter-spacing: 3px; }
  .product-gummies { top: 306px; font-size: 108px; letter-spacing: 2px; }
  .flavor-bar {
    position: absolute; left: 116px; top: 405px; width: 330px; height: 38px;
    background: var(--pink); color: var(--white);
    font-weight: 500; font-size: 26px; line-height: 38px; padding-left: 12px;
  }
  .dose {
    position: absolute; left: 0; width: 552px; text-align: center;
    color: var(--white); font-weight: 900; text-transform: uppercase;
    text-shadow:
      -2px -2px 0 var(--navy), 2px -2px 0 var(--navy),
      -2px 2px 0 var(--navy), 2px 2px 0 var(--navy),
      0 4px 0 var(--navy);
  }
  .dose-servings { top: 602px; font-size: 34px; }
  .dose-amount { top: 642px; font-size: 52px; }
  .info-band {
    position: absolute; left: 0; top: 837px; width: 552px; height: 248px;
    background: var(--navy-deep);
  }
  .compliance-mark { position: absolute; left: 30px; top: 40px; width: 90px; height: 90px; }
  .kids-warning-mark {
    position: absolute; left: 158px; top: 42px; width: 90px; height: 118px;
    background: var(--white); padding: 5px;
  }
  .kids-warning-mark div { width: 100%; height: 100%; background: var(--red); }
  .warning-copy {
    position: absolute; left: 268px; top: 66px; width: 270px;
    color: var(--white); font-weight: 600; font-size: 9.6px;
    line-height: 16px; text-transform: uppercase; letter-spacing: 0.2px;
  }
</style>
</head>
<body>
  <div class="label">
    <div class="fruit-backdrop" role="img" aria-label="Photograph of assorted fresh berries and fruit"></div>

    <svg class="pennant" viewBox="0 0 371 535" aria-hidden="true">
      <polygon points="0,0 371,0 371,405 185.5,535 0,405" fill="var(--navy)"/>
      <polyline points="12,0 12,398 185.5,518 359,398 359,0" fill="none" stroke="var(--white)" stroke-width="5"/>
    </svg>

    <div class="brand">
      <div class="brand-mark"></div>
      <div class="brand-name">Lark Hollow<span>Edibles</span></div>
    </div>

    <div class="product-thc">THC</div>
    <div class="product-gummies">GUMMIES</div>
    <div class="flavor-bar">Assorted flavors</div>

    <div class="dose dose-servings">10 Servings per pack</div>
    <div class="dose dose-amount">50mg per pack</div>

    <div class="info-band">
      <svg class="compliance-mark" viewBox="0 0 90 90" aria-hidden="true">
        <polygon points="45,6 86,80 4,80" fill="none" stroke="var(--white)" stroke-width="7" stroke-linejoin="round"/>
      </svg>
      <div class="kids-warning-mark" aria-hidden="true"><div></div></div>
      <p class="warning-copy">Keep out of the reach of children. Contains desiccant packet for freshness. Do not eat packet. Do not use if safety seal is damaged or missing. Store in a cool, dry place.</p>
    </div>
  </div>
</body>
</html>
```